Energy trading company (Voltarix) needs a business card

We need a business card for a company based in Central America. Our main purpose is trading energy . We already have the logo but we need some good creativity to design a high impact business card. Colors blue, orange, green can be used or we would like to see good combinatios with our logo

Target Market(s)

Energy

Industry/Entity Type

Power Generation

Contact Information for Business Card

Logo , headquarters , name, background

Font styles to use
Serif
Sans Serif

Colors

Designer to choose colors to be used in the design.

Requirements
Must have
• it must have a fresh and clean view
Nice to have
• good backgrounds that combine with the logo
Should not have
• too much words

```html
<!DOCTYPE html>
<html lang="en">
<head>
<meta charset="utf-8">
<title>Voltarix Business Card</title>
<link rel="stylesheet" href="https://fonts.googleapis.com/css2?family=Open+Sans:wght@400;600&display=swap">
<style>
  :root {
    --bg: #b9b9b9;
    --orange: #f0911f;
    --orange-deep: #c9741b;
    --orange-faint: #f6e6d2;
    --white: #ffffff;
    --paper-top: #e6e6e6;
    --ink: #2b2b2b;
  }
  html, body {
    margin: 0;
    width: 1200px;
    height: 900px;
    overflow: hidden;
    background: var(--bg);
    font-family: "Open Sans", sans-serif;
  }
  .stage {
    position: relative;
    width: 1200px;
    height: 900px;
  }
  .card {
    position: absolute;
    left: 320px;
    width: 560px;
    height: 320px;
    box-shadow: 0 6px 18px rgba(0,0,0,0.25);
    overflow: hidden;
  }
  /* Front */
  .card-front {
    top: 90px;
    background: linear-gradient(160deg, var(--orange-deep) 0%, var(--orange) 100%);
  }
  .streaks {
    position: absolute;
    right: 0;
    top: 0;
    width: 300px;
    height: 200px;
    background: radial-gradient(ellipse at 100% 20%, rgba(255,255,255,0.28) 0%, rgba(255,255,255,0.08) 55%, rgba(255,255,255,0) 80%);
  }
  .front-brand {
    position: absolute;
    left: 50px;
    top: 150px;
    display: flex;
    align-items: center;
    gap: 16px;
  }
  .brand-dot {
    width: 70px;
    height: 70px;
    border-radius: 50%;
    background: var(--white);
  }
  .front-name {
    color: var(--white);
    font-size: 34px;
    font-weight: 600;
    letter-spacing: 1px;
  }
  .front-url {
    position: absolute;
    left: 300px;
    top: 120px;
    color: var(--white);
    font-size: 14px;
    letter-spacing: 0.5px;
    opacity: 0.9;
  }
  /* Back */
  .card-back {
    top: 490px;
    background: linear-gradient(200deg, var(--paper-top) 0%, var(--white) 55%);
  }
  .faint-mark {
    position: absolute;
    right: 40px;
    top: 30px;
    display: flex;
    align-items: center;
    gap: 12px;
  }
  .faint-dot {
    width: 130px;
    height: 130px;
    border-radius: 50%;
    background: var(--orange-faint);
  }
  .faint-name {
    color: var(--orange-faint);
    font-size: 26px;
    font-weight: 600;
  }
  .back-brand {
    position: absolute;
    left: 36px;
    top: 34px;
    display: flex;
    align-items: center;
    gap: 10px;
  }
  .brand-dot-small {
    width: 32px;
    height: 32px;
    border-radius: 50%;
    background: var(--orange);
  }
  .back-name {
    color: var(--orange);
    font-size: 30px;
    font-weight: 400;
    letter-spacing: 1px;
  }
  .person {
    position: absolute;
    left: 36px;
    top: 100px;
  }
  .person-name {
    color: var(--orange);
    font-size: 19px;
    font-weight: 600;
    margin: 0;
  }
  .person-role {
    color: var(--ink);
    font-size: 14px;
    margin: 0 0 14px;
  }
  .address {
    color: var(--ink);
    font-size: 14px;
    line-height: 1.35;
    margin: 0 0 8px;
    font-style: normal;
  }
  .contact {
    list-style: none;
    margin: 0;
    padding: 0;
    color: var(--ink);
    font-size: 14px;
    line-height: 1.45;
  }
  .contact li {
    display: flex;
    align-items: center;
    gap: 8px;
  }
  .contact svg {
    width: 12px;
    height: 12px;
    fill: none;
    stroke: var(--orange);
    stroke-width: 1.8;
  }
</style>
</head>
<body>
<div class="stage">
  <section class="card card-front">
    <div class="streaks" role="img" aria-label="Fine light streaks radiating across the orange background"></div>
    <div class="front-brand">
      <span class="brand-dot"></span>
      <span class="front-name">VOLTARIX</span>
    </div>
    <span class="front-url">www.voltarix.com</span>
  </section>

  <section class="card card-back">
    <div class="faint-mark">
      <span class="faint-dot"></span>
      <span class="faint-name">VOLTARIX</span>
    </div>
    <div class="back-brand">
      <span class="brand-dot-small"></span>
      <span class="back-name">VOLTARIX</span>
    </div>
    <div class="person">
      <p class="person-name">Marco Ellison</p>
      <p class="person-role">Founder</p>
      <address class="address">48 Harbor Lane, Suite 310<br>Port Alder, Florida, 30412</address>
      <ul class="contact">
        <li><svg viewBox="0 0 12 12"><path d="M3 1 L5 3.5 L4 5 Q5.5 7.5 7 8 L8.5 7 L11 9 L9.5 11 Q4 10 1 3 Z"/></svg>(555) 218-4470</li>
        <li><svg viewBox="0 0 12 12"><rect x="1" y="2.5" width="10" height="7"/><path d="M1 2.5 L6 6.5 L11 2.5"/></svg>marco@voltarix.com</li>
        <li><svg viewBox="0 0 12 12"><circle cx="6" cy="6" r="5"/><path d="M1 6 H11 M6 1 Q3 6 6 11 Q9 6 6 1"/></svg>www.voltarix.com</li>
      </ul>
    </div>
  </section>
</div>
</body>
</html>
```